Iconic website for iconic products

We want a website which will stand out, which will reflect that we are offering cutting edge solutions, breaking the mould. The website must be very search engine friendly, to drive traffic from all around the world, and also sticky, so that they explore what we have to offer, and hopefully buy from us.

We have launched a portfolio of products in the field of 3D, which are highly accessible. They are accessible in their openness, their ease of use and their ultra low cost. We are providing everyone everywhere the opportunity to engage in 3D design and to produce physical 3D models as outputs from their designs. This technology is ground breaking and world changing.

The website will need to be easy for us to maintain and grow, easy for our customers and prospects to use, easy to find.

We will need to integrate a blog, and provide eCommerce capability. We will also be looking to add a forum, which we will need to monitor and maintain, so that our customers can connect with one another, share best practice, offer solutions to problems, and generate value for one another, while reducing our after-sales support burden.

We will also need to set up page templates for our key customers to show what they have done with our products so that others can share the experience.

Target Market(s)

We have a number of distinct markets.
Education:
Primary (5-11) schools
Secondary (11-18) schools
Colleges (16-19)
Universities
Creative designers and designer-makers
Industrial companies; any that are involved in design, in manufacture, in marketing
Animation, games and virtual world organisations
Hobbyists

Industry/Entity Type

Sales

Requirements
Must have
• Iconic design
• Ease of maintenance and future build
• Blog
• eCommerce
• Forum
• Chirpline
• When people enquire, people must fill in forms to download information, and we must capture that information on a database.
• We also need a secure log in area for distributors and resellers to access for confidential information.
Nice to have
• An updated logo to match the website
Should not have
• Old fashioned design
• Bricks and mortar feel

```html
<!DOCTYPE html>
<html lang="en">
<head>
<meta charset="utf-8">
<title>Aspera Technologies</title>
<link href="https://fonts.googleapis.com/css2?family=Ubuntu:wght@400;500;700&family=Questrial&family=Open+Sans:wght@400;600;700&family=Satisfy&display=swap" rel="stylesheet">
<style>
:root{
  --red:#b3171a;
  --red-dark:#8c0c0e;
  --red-deep:#6e0708;
  --head-red:#a31414;
  --charcoal:#262626;
  --ink:#222;
  --grey-band:#cfcfcf;
  --white:#fff;
  --line:#d9d9d9;
}
*{margin:0;padding:0;box-sizing:border-box}
html,body{width:684px;height:1200px;overflow:hidden}
body{position:relative;font-family:"Open Sans",sans-serif;color:var(--ink);background:var(--red)}
.abs{position:absolute}

/* navigation */
.topnav{left:0;top:0;width:684px;height:27px;background:linear-gradient(#c5181b,#9f0c0e)}
.topnav ul{position:absolute;left:283px;top:0;display:flex;list-style:none;height:27px;align-items:center;font-family:"Ubuntu",sans-serif;font-weight:500;font-size:8.5px;color:var(--white)}
.topnav li{padding:0 7px;line-height:27px;position:relative}
.topnav li+li::before{content:"|";position:absolute;left:-2px;opacity:.7}
.topnav li.active{background:var(--charcoal)}

/* header */
.header{left:0;top:27px;width:684px;height:77px;background:linear-gradient(#333,#1e1e1e);border-bottom:1px solid #3c3c3c}
.brand{left:73px;top:6px;display:flex;align-items:center;gap:7px}
.brand-mark{width:64px;height:63px;background:#c8282a}
.brand-name{font-family:"Ubuntu",sans-serif;font-weight:500;font-size:21px;color:var(--white)}
.tagline{right:73px;top:25px;text-align:right;font-family:"Satisfy",cursive;color:#eee;font-size:11.5px;line-height:17px}
.tagline b{font-family:"Ubuntu",sans-serif;font-size:14px}

/* hero */
.hero{left:0;top:104px;width:684px;height:236px;background:linear-gradient(90deg,#0b3a55 0%,#0f2231 18%,#2a0a05 45%,#3a0a04 70%,#b2250f 90%,#d8461c 100%)}
.hero-frame{left:73px;top:12px;width:538px;height:210px;background:var(--white);border-radius:4px;padding:5px}
.hero-photo{width:100%;height:100%;background:linear-gradient(90deg,#2c1004,#4a1f0a 50%,#2c1004);border-radius:2px}
.arrow{top:105px;width:25px;height:25px;background:linear-gradient(#e8e8e8,#bdbdbd);border-radius:3px;display:flex;align-items:center;justify-content:center}
.arrow.prev{left:61px}.arrow.next{left:597px}

/* follow band */
.follow{left:0;top:340px;width:684px;height:89px;background:linear-gradient(#bdbdbd,#e3e3e3)}
.follow h3,.login h3{font-family:"Ubuntu",sans-serif;font-weight:500;font-size:11px;color:#111}
.follow h3{position:absolute;left:73px;top:8px}
.social{top:28px;width:52px;height:52px;border-radius:6px;display:flex;align-items:center;justify-content:center;font-family:"Open Sans",sans-serif;font-weight:700;font-size:7.5px;color:var(--white)}
.social.chirp{left:73px;background:#55c2e6}
.social.friend{left:145px;background:#3b5a98}
.social.feed{left:223px;background:#f1782b}
.social.chat{left:303px;width:64px;background:none}
.login{left:449px;top:5px;width:150px}
.login h3{position:absolute;left:27px;top:3px}
.field{position:absolute;left:3px;width:130px;height:16px;background:var(--white);border:1px solid #888;font-size:6.5px;color:#999;padding:3px 4px}
.btn-login{position:absolute;left:2px;top:61px;width:44px;height:14px;background:linear-gradient(#c32a2c,#8e0f10);border-radius:3px;color:var(--white);font-family:"Ubuntu",sans-serif;font-size:7.5px;text-align:center;line-height:14px}
.forgot{position:absolute;left:72px;top:63px;font-size:6px;color:#b01010}

/* main */
.page{left:0;top:429px;width:684px;height:747px;background:linear-gradient(90deg,#b81d21,#cc3135 30%,#b81d21 60%,#c72c30)}
.column{left:68px;top:429px;width:548px;height:747px;background:var(--white)}
.content{left:79px;width:327px}
.content h2{font-family:"Questrial",sans-serif;font-weight:400;color:var(--head-red);font-size:15px}
.content p{font-size:7.2px;line-height:11px}
.more{font-size:6.6px;font-weight:700;display:flex;align-items:center;gap:3px}
.more i{width:7px;height:7px;background:var(--red-dark);display:inline-block;clip-path:polygon(0 0,100% 50%,0 100%)}
.more i{clip-path:none;position:relative}
.more i::after{content:"";position:absolute;left:2px;top:1.5px;border-left:3px solid #fff;border-top:2px solid transparent;border-bottom:2px solid transparent}
.price{left:345px;top:693px;font-size:7.5px;font-weight:700}
.product-photo{left:286px;top:706px;width:120px;height:88px;border:1px solid #555;background:linear-gradient(135deg,#3a4f7a,#8c8f96 50%,#d9d3c8)}
.wow{left:79px;top:787px;font-size:7.2px;font-weight:600}
.benefits{left:79px;top:800px;list-style:none;font-size:7.2px;line-height:14.5px}
.benefits li::before{content:"»";color:var(--red);font-weight:700;margin-right:4px}
.card{left:73px;width:321px;height:67px;background:#f6f6f6}
.card h4{position:absolute;left:14px;top:5px;font-family:"Questrial",sans-serif;font-weight:400;color:var(--head-red);font-size:11.5px}
.card .lead{position:absolute;left:14px;top:22px;font-size:7.3px;font-weight:600}
.card .sub{position:absolute;left:14px;top:33px;font-size:7.3px}
.card .cta{position:absolute;left:14px;top:50px;font-size:6.8px;font-weight:700}
.card .thumb{position:absolute;left:223px;top:2px;width:79px;height:63px;border:1px solid #444}

/* sidebar */
.panel{left:451px;width:160px;background:linear-gradient(#d8383b,#c12528);border:1px solid #e06a6c;color:var(--white)}
.panel h3{position:absolute;font-family:"Ubuntu",sans-serif;font-weight:700;font-size:14px}
.panel label{position:absolute;left:10px;font-size:6.8px;font-weight:600}
.panel .input{position:absolute;left:10px;width:139px;height:16px;background:var(--white);border:1px solid #e0a0a0}
.panel .button{position:absolute;top:210px;width:52px;height:17px;background:linear-gradient(#fff,#d8d8d8);border:1px solid #999;color:#222;font-size:7px;font-weight:700;text-align:center;line-height:15px}
.post-img{position:absolute;left:8px;width:69px;height:47px}
.post-meta{position:absolute;left:85px;font-size:7px;font-weight:600;line-height:8.5px}
.post-excerpt{position:absolute;left:8px;width:145px;font-size:6.8px;font-weight:600;line-height:8.7px}
.post-more{position:absolute;right:14px;font-size:6.6px;font-weight:700}
.dots{position:absolute;left:8px;top:136px;width:141px;border-top:1px dotted #fff}
.video{position:absolute;left:15px;top:29px;width:130px;height:103px;background:#111}
.video-still{width:130px;height:87px;background:linear-gradient(#5a2a18,#2b2a6a 55%,#1a1a2a)}
.video-bar{height:16px;background:#eee;display:flex;align-items:center;gap:5px;padding:0 5px;font-size:4.5px;color:#555}

/* footer */
.footer{left:0;top:1176px;width:684px;height:24px;background:var(--red-deep);color:var(--white);font-size:6.2px;font-weight:700;font-family:"Open Sans",sans-serif}
.footer .copy{position:absolute;left:79px;top:7px}
.footer .links{position:absolute;right:79px;top:7px}
</style>
</head>
<body>

<nav class="abs topnav">
  <ul>
    <li class="active">Home</li><li>Product</li><li>Gallery</li><li>News</li><li>Contact</li><li>Order</li><li>Forum</li>
  </ul>
</nav>

<header class="abs header">
  <div class="abs brand"><span class="brand-mark"></span><span class="brand-name">Aspera Technologies</span></div>
  <div class="abs tagline">Incredibly low cost <b>3D</b> technologies<br>for designing and producing 3d models</div>
</header>

<section class="abs hero">
  <div class="abs hero-frame"><div class="hero-photo" role="img" aria-label="Three views of a 3D printed bust in cream material on a dark brown backdrop"></div></div>
  <div class="abs arrow prev"><svg width="12" height="14" viewBox="0 0 12 14"><path d="M9 1 3 7l6 6" fill="none" stroke="#222" stroke-width="3"/></svg></div>
  <div class="abs arrow next"><svg width="12" height="14" viewBox="0 0 12 14"><path d="M3 1l6 6-6 6" fill="none" stroke="#222" stroke-width="3"/></svg></div>
</section>

<section class="abs follow">
  <h3>Follow Us on!</h3>
  <div class="abs social chirp">Chirpline</div>
  <div class="abs social friend">Friendbook</div>
  <div class="abs social feed">Feed</div>
  <div class="abs social chat">
    <svg width="64" height="52" viewBox="0 0 64 52">
      <path d="M4 20c0-10 10-16 21-16s21 6 21 16-10 16-21 16c-3 0-5 0-7-1L8 42l3-9c-4-3-7-8-7-13z" fill="#f28a1a" stroke="#222" stroke-width="2"/>
      <path d="M22 30c0-9 9-14 19-14s19 5 19 14c0 5-3 9-7 12l3 9-10-6c-2 0-3 1-5 1-10 0-19-6-19-16z" fill="#3b8fe0" stroke="#222" stroke-width="2"/>
    </svg>
  </div>
  <div class="abs login">
    <svg class="abs" style="left:0;top:0" width="20" height="18" viewBox="0 0 20 18"><path d="M5 8V5a4 4 0 0 1 8 0v3" fill="none" stroke="#999" stroke-width="2"/><rect x="2" y="8" width="14" height="9" rx="1" fill="#d9b24c"/></svg>
    <h3>Member Login</h3>
    <div class="field" style="top:19px">Email id:</div>
    <div class="field" style="top:39px">Password:</div>
    <div class="btn-login">Log In</div>
    <div class="forgot">Forgot Password?</div>
  </div>
</section>

<div class="abs page"></div>
<main class="abs column"></main>

<h2 class="abs content" style="top:455px;font-family:'Questrial',sans-serif;font-weight:400;color:var(--head-red);font-size:15px">Welcome to Aspera Technologies</h2>
<p class="abs content" style="top:482px;font-size:7.2px;line-height:11px">Lorem Ipsum is simply dummy text of the printing and typesetting industry. Lorem Ipsum has been the industry's standard dummy text ever since the 1500s, when an unknown printer took a galley of type and scrambled it to make a type specimen book.</p>
<p class="abs content" style="top:537px;font-size:7.2px;line-height:11px">It has survived not only five centuries, but also the leap into electronic typesetting, remaining essentially unchanged. It was popularised in the 1960s with the release of Typeset sheets containing Lorem Ipsum passages, and more recently with desktop publishing software like Pagecraft Studio including versions of Lorem Ipsum.</p>
<div class="abs content more" style="top:588px"><i></i>Read More</div>

<h2 class="abs content" style="top:620px;font-family:'Questrial',sans-serif;font-weight:400;color:var(--head-red);font-size:15px">Our Products Range</h2>
<p class="abs content" style="top:646px;font-size:7.2px">below are our full range of products..</p>

<h2 class="abs content" style="top:680px;font-family:'Questrial',sans-serif;font-weight:400;color:var(--head-red);font-size:15px">KESTREL 3D creative solution</h2>
<div class="abs price">PRICE: £ 495.00</div>
<p class="abs" style="left:79px;top:704px;width:196px;font-size:7.2px;line-height:11px">The easy way to design creative 3D models on a PC without having to learn or use 3D CAD.<br><br>Kestrel is a cutting edge ‘haptic’ technology which delivers a high quality, immersive 3D ....</p>
<div class="abs product-photo" role="img" aria-label="Laptop showing a 3D model beside a haptic stylus device"></div>
<div class="abs wow">Kestrel’s WOW factors:</div>
<ul class="abs benefits">
  <li>Use our 3D mouse to ‘touch’ and feel the 3 dimensional qualities of a virtual object</li>
  <li>Movement in all directions to manipulate and construct objects within a 3D space</li>
  <li>Sense of touching and moving freely, tapping into your natural way of doing things</li>
  <li>Feel where you are, whether inside or outside objects</li>
  <li>So easy to create organic shapes</li>
  <li>Change the hardness/softness of virtual objects for different effects</li>
  <li>Straightforward interface for a more intuitive way to sketch and model</li>
</ul>
<div class="abs content more" style="top:907px"><i></i>Other Products</div>

<article class="abs card" style="top:941px">
  <h4>Kestrel 3D creative</h4>
  <div class="lead">package from £350</div>
  <div class="sub">for designing creative 3D models</div>
  <div class="cta">Click for more information</div>
  <div class="thumb" role="img" aria-label="Cream 3D printed ring model on a dark blue background" style="background:radial-gradient(ellipse at center,#d9dcd0 0%,#9aa3b5 40%,#23306a 75%)"></div>
</article>
<article class="abs card" style="top:1021px">
  <h4>Orin 3D Laserscanner</h4>
  <div class="lead">from £320</div>
  <div class="sub">for creating virtual 3D models from real objects</div>
  <div class="cta">Click for more information</div>
  <div class="thumb" role="img" aria-label="Three scanned figurine models in tan material" style="background:linear-gradient(90deg,#f3eadc,#c9995c 30%,#f3eadc 50%,#c9995c 70%,#f3eadc)"></div>
</article>
<div class="abs content more" style="top:1111px"><i></i>Other Products</div>

<aside class="abs panel" style="top:459px;height:237px">
  <svg class="abs" style="left:7px;top:3px" width="30" height="28" viewBox="0 0 30 28"><rect x="3" y="6" width="18" height="20" fill="#fff" transform="rotate(-15 12 16)"/><path d="M14 18 27 3" stroke="#e0b040" stroke-width="3"/></svg>
  <h3 style="left:44px;top:9px">Enquiry Now</h3>
  <label style="top:34px">Name</label><div class="input" style="top:41px"></div>
  <label style="top:68px">E-mail</label><div class="input" style="top:77px"></div>
  <label style="top:102px">Subject</label><div class="input" style="top:114px"></div>
  <label style="top:136px">Comments</label><div class="input" style="top:144px;height:61px"></div>
  <div class="button" style="left:27px">Submit</div>
  <div class="button" style="left:83px">Clear</div>
</aside>

<aside class="abs panel" style="top:716px;height:251px">
  <svg class="abs" style="left:8px;top:3px" width="29" height="29" viewBox="0 0 29 29"><rect width="29" height="29" rx="5" fill="#f1782b"/><circle cx="8" cy="21" r="3" fill="#fff"/><path d="M6 12a11 11 0 0 1 11 11M6 6a17 17 0 0 1 17 17" fill="none" stroke="#fff" stroke-width="3"/></svg>
  <h3 style="left:45px;top:10px">Recent Blog Post</h3>
  <div class="post-img" style="top:44px;background:linear-gradient(90deg,#2b5fa8,#6f8fc0 60%,#d8d8d8)" role="img" aria-label="Blog post image about fair pricing"></div>
  <div class="post-meta" style="top:47px">Topic By<br>M.R. Dalton<br><span style="font-weight:400">01-05-2010</span></div>
  <div class="post-excerpt" style="top:95px">Lorem Ipsum is simply dummy text of the printing and typesetting industry.</div>
  <div class="post-more" style="top:125px">Read More</div>
  <div class="dots"></div>
  <div class="post-img" style="top:148px;background:linear-gradient(135deg,#f2f2f2,#c9cfd6)" role="img" aria-label="Blog post image in soft grey tones"></div>
  <div class="post-meta" style="top:151px">Topic By<br>Pia L.<br><span style="font-weight:400">30-04-2010</span></div>
  <div class="post-excerpt" style="top:199px">It has survived not only five centuries, but also the leap into electronic typesetting, remaining essentially unchanged.</div>
  <div class="post-more" style="top:237px">Read More</div>
</aside>

<aside class="abs panel" style="top:986px;left:450px;height:153px">
  <svg class="abs" style="left:4px;top:4px" width="28" height="22" viewBox="0 0 28 22"><rect x="1" y="5" width="26" height="16" rx="3" fill="#333"/><rect x="8" y="1" width="10" height="5" fill="#333"/><circle cx="14" cy="13" r="5" fill="#777" stroke="#111" stroke-width="2"/></svg>
  <h3 style="left:37px;top:7px;font-size:15px">Video Section</h3>
  <div class="video">
    <div class="video-still" role="img" aria-label="Video still of a desktop 3D printer lit in blue">
      <svg style="margin:35px 0 0 57px" width="16" height="16" viewBox="0 0 16 16"><path d="M3 1l12 7-12 7z" fill="#fff"/></svg>
    </div>
    <div class="video-bar">
      <svg width="7" height="7" viewBox="0 0 7 7"><path d="M0 0l7 3.5L0 7z" fill="#333"/></svg>
      <span>00:00</span>
      <span style="flex:1;height:4px;background:#ccc;border-radius:2px"></span>
      <span>Watch</span>
    </div>
  </div>
  <div class="abs" style="left:0;top:137px;width:160px;text-align:center;font-size:6.8px;font-weight:700">More Videos</div>
</aside>

<footer class="abs footer">
  <div class="copy">Copyright© Aspera Technologies Ltd 2009-2010 &nbsp;|&nbsp; All Rights Reserved.</div>
  <div class="links">Contact Us | Privacy | Sitemap</div>
</footer>

</body>
</html>
```